New business card for civil engineering company - "Keystone Audit"

We need a business card designed for our new structural engineering company.

The company name is "Keystone Audit" logo files attached.

We would like the following:
* Two-sided card
* Simple design

Information to be placed on the card:
Name - Marcus Dellow
Job Title - Director / Structural Engineer
Credentials - BEng(Hons), CPEng, CMengNZ, IntPE(NZ)
Email - marcus.dellow@keystoneaudit.co.nz
mobile - 0219364058
website - www.keystoneaudit.co.nz

```html
<!DOCTYPE html>
<html lang="en">
<head>
<meta charset="utf-8">
<title>Keystone Audit – Business Card</title>
<link rel="stylesheet" href="https://fonts.googleapis.com/css2?family=Open+Sans:wght@400;600;700;800&display=swap">
<style>
  :root {
    --bg: #232323;
    --brand-blue: #3a8fcd;
    --accent-blue: #2f86d1;
    --ink: #333538;
    --ink-soft: #4a4d52;
    --card-white: #ffffff;
    --rule: #3b3d40;
  }
  * { box-sizing: border-box; margin: 0; padding: 0; }
  html, body {
    width: 1200px; height: 900px; overflow: hidden;
    background: var(--bg);
    font-family: "Open Sans", Arial, sans-serif;
  }
  .stage {
    position: relative; width: 1200px; height: 900px;
    display: flex; flex-direction: column; align-items: center; justify-content: center; gap: 50px;
  }
  .card {
    position: relative; width: 560px; height: 320px;
    box-shadow: 0 10px 30px rgba(0,0,0,.45);
  }
  /* Front */
  .card-front {
    background: var(--brand-blue);
    display: flex; align-items: center; justify-content: center;
  }
  .front-wordmark {
    display: flex; align-items: center; gap: 12px;
    color: #fff; font-weight: 600; font-size: 30px; letter-spacing: 3px; text-transform: uppercase;
  }
  .front-wordmark .mark-square { width: 18px; height: 18px; background: #fff; }
  /* Back */
  .card-back { background: var(--card-white); color: var(--ink); }
  .back-wordmark {
    position: absolute; right: 40px; top: 62px;
    display: flex; align-items: center; gap: 8px;
    color: var(--accent-blue); font-weight: 600; font-size: 17px; letter-spacing: 2px; text-transform: uppercase;
  }
  .back-wordmark .mark-square { width: 11px; height: 11px; background: var(--accent-blue); }
  .rule-long {
    position: absolute; left: 250px; right: 36px; top: 134px;
    height: 2px; background: var(--rule);
  }
  .identity { position: absolute; left: 40px; top: 146px; }
  .person-name { font-size: 34px; font-weight: 800; line-height: 1.05; color: var(--ink); }
  .person-role { font-size: 16px; font-weight: 600; color: var(--accent-blue); margin-top: 2px; }
  .rule-short { width: 215px; height: 2px; background: var(--rule); margin-top: 8px; }
  .contacts { list-style: none; margin-top: 10px; }
  .contacts li {
    display: flex; align-items: center; gap: 9px;
    font-size: 14px; color: var(--ink-soft); line-height: 22px;
  }
  .contacts svg { width: 12px; height: 12px; flex: none; }
  .credentials {
    position: absolute; right: 36px; top: 150px;
    text-align: right; font-size: 13px; line-height: 20px; color: var(--ink-soft);
  }
</style>
</head>
<body>
<main class="stage">
  <section class="card card-front" aria-label="Card front">
    <div class="front-wordmark"><span class="mark-square"></span>Keystone Audit</div>
  </section>

  <section class="card card-back" aria-label="Card back">
    <div class="back-wordmark"><span class="mark-square"></span>Keystone Audit</div>
    <div class="rule-long"></div>
    <div class="credentials">BEng(Hons), CPEng,<br>CMengNZ, IntPE(NZ)</div>
    <div class="identity">
      <h1 class="person-name">Marcus Dellow</h1>
      <p class="person-role">Director / Structural Engineer</p>
      <div class="rule-short"></div>
      <ul class="contacts">
        <li>
          <svg viewBox="0 0 24 24" aria-hidden="true"><path fill="#2f86d1" d="M6.6 10.8a15.1 15.1 0 0 0 6.6 6.6l2.2-2.2a1 1 0 0 1 1-.25 11.4 11.4 0 0 0 3.6.57 1 1 0 0 1 1 1V20a1 1 0 0 1-1 1A17 17 0 0 1 3 4a1 1 0 0 1 1-1h3.5a1 1 0 0 1 1 1c0 1.25.2 2.45.57 3.57a1 1 0 0 1-.25 1z"/></svg>
          0219364058
        </li>
        <li>
          <svg viewBox="0 0 24 24" aria-hidden="true"><rect x="2" y="5" width="20" height="14" rx="1.5" fill="#2f86d1"/><path d="M3 6l9 7 9-7" stroke="#fff" stroke-width="1.8" fill="none"/></svg>
          marcus.dellow@keystoneaudit.co.nz
        </li>
        <li>
          <svg viewBox="0 0 24 24" aria-hidden="true"><circle cx="12" cy="12" r="10" fill="#2f86d1"/><path d="M2 12h20M12 2c3 3 3 17 0 20M12 2c-3 3-3 17 0 20" stroke="#fff" stroke-width="1.5" fill="none"/></svg>
          www.keystoneaudit.co.nz
        </li>
      </ul>
    </div>
  </section>
</main>
</body>
</html>
```